REDESIGN COUPLE PAGES FOR SURGE VIDEO ADS

PLEASE REDESIGN THIS PAGE FOR ME:
http://pagekitfinder.com/rk/milo/surge/pricing.html
I need it to be easy to read for the end user so the customer knows exactly what he will be getting. Make an emphasis on the subscription as the most popular item....and also the price per video format should be emphasized too.

Target Market(s)

B2B

Industry/Entity Type

Video Production

Number of Pages Required

3 page

Colors

Designer to choose colors to be used in the design.

Requirements
Must have
• PLEASE REDESIGN THIS PAGE FOR ME:
• http://pagekitfinder.com/rk/milo/surge/pricing.html
• I need it to be easy to read for the end user so the customer knows exactly what he will be getting. Make an emphasis on the subscription as the most popular item....and also the price per video format should be emphasized too.
Nice to have
Should not have

```html
<!DOCTYPE html>
<html lang="en">
<head>
<meta charset="utf-8">
<title>SURGE – Pricing</title>
<link rel="stylesheet" href="https://fonts.googleapis.com/css2?family=Fira+Sans:ital,wght@0,400;0,500;0,600;1,400;1,700&family=Lato:wght@400;700&display=swap">
<style>
  :root {
    --navy: #141d2f;
    --ink: #1c2233;
    --muted: #6b7280;
    --sky: #63cbf4;
    --sky-strip: #4fb5ea;
    --royal: #2453d3;
    --royal-strip: #1e44b8;
    --tab-text: #2451cf;
    --price: #e2444f;
    --line: #e4e8ee;
    --panel: #f9fafb;
    --btn-a: #3ba9ea;
    --btn-b: #2a5ed6;
    --white: #ffffff;
  }
  * { box-sizing: border-box; margin: 0; padding: 0; }
  html, body { width: 1200px; height: 1111px; overflow: hidden; background: var(--white); }
  body { position: relative; font-family: "Fira Sans", sans-serif; color: var(--ink); }

  /* Header */
  .site-header { position: absolute; left: 0; top: 0; width: 1200px; height: 49px; background: var(--navy); }
  .brand { position: absolute; left: 172px; top: 9px; color: var(--white); }
  .brand-name { font-family: "Fira Sans", sans-serif; font-weight: 600; font-size: 19px; letter-spacing: 3px; line-height: 20px; color: #dfe6ee; }
  .brand-tag { font-size: 5.5px; letter-spacing: .6px; color: #cfd6df; margin-top: 1px; }
  .main-nav { position: absolute; top: 0; left: 434px; height: 49px; display: flex; align-items: center; gap: 15px; font-family: "Lato", sans-serif; font-size: 10px; }
  .main-nav a { color: var(--white); text-decoration: none; }
  .main-nav a.active { color: #3f8ff0; }
  .account { position: absolute; right: 172px; top: 12px; display: flex; align-items: center; gap: 12px; font-family: "Lato", sans-serif; font-size: 9.5px; }
  .account .login { color: var(--white); }
  .account .signup { background: #2f86e8; color: var(--white); width: 52px; height: 24px; display: flex; align-items: center; justify-content: center; border: 1px solid #5aa4f2; }

  /* Heading */
  .page-title { position: absolute; top: 94px; width: 1200px; text-align: center; font-family: "Lato", sans-serif; font-weight: 700; font-size: 23px; letter-spacing: .5px; color: var(--ink); }
  .page-subtitle { position: absolute; top: 125px; width: 1200px; text-align: center; font-family: "Lato", sans-serif; font-size: 15px; letter-spacing: .4px; color: var(--ink); }

  /* Plans */
  .plan { position: absolute; left: 253px; width: 694px; height: 68px; background: var(--white); border: 1px solid var(--line); border-radius: 4px; }
  .plan-tab { position: absolute; left: -1px; top: -1px; width: 229px; height: 68px; background: var(--sky);
    clip-path: polygon(0 0, 219px 0, 219px 42%, 229px 50%, 219px 58%, 219px 100%, 0 100%); border-radius: 4px 0 0 4px; }
  .plan-strip { position: absolute; left: 0; top: 0; width: 19px; height: 100%; background: var(--sky-strip); display: flex; align-items: center; justify-content: center; }
  .chevron { width: 4px; height: 4px; border-right: 1px solid var(--tab-text); border-bottom: 1px solid var(--tab-text); transform: rotate(45deg); }
  .plan-name { position: absolute; left: 38px; top: 19px; font-size: 15px; font-weight: 500; color: var(--tab-text); letter-spacing: .3px; line-height: 16px; }
  .plan-note { position: absolute; left: 38px; top: 39px; font-size: 9px; color: var(--tab-text); }
  .plan-lead { position: absolute; right: 380px; top: 28px; font-size: 9px; font-style: italic; color: var(--muted); }
  .plan-price { position: absolute; right: 238px; top: 21px; font-size: 19px; color: var(--price); line-height: 22px; }
  .plan-price sup { font-size: 10px; vertical-align: 8px; }
  .plan-unit { position: absolute; left: 475px; top: 28px; font-size: 9.5px; color: var(--muted); }
  .buy-btn { position: absolute; width: 87px; height: 35px; display: flex; align-items: center; justify-content: center;
    background: linear-gradient(90deg, var(--btn-a), var(--btn-b)); color: var(--white); font-weight: 600; font-size: 9.5px; border-radius: 2px; }
  .plan .buy-btn { left: 587px; top: 16px; }

  .plan--featured { left: 247px; width: 706px; height: 81px; top: 265px; border: none; border-radius: 4px; box-shadow: 0 4px 18px rgba(30,50,90,.12); z-index: 2; }
  .plan--featured .plan-tab { left: 0; top: 0; width: 235px; height: 81px; background: var(--royal);
    clip-path: polygon(0 0, 225px 0, 225px 42%, 235px 50%, 225px 58%, 225px 100%, 0 100%); }
  .plan--featured .plan-strip { width: 31px; background: var(--royal-strip); }
  .plan--featured .chevron { border-color: var(--white); transform: rotate(-135deg); margin-top: 3px; }
  .plan--featured .plan-name { left: 43px; top: 20px; font-size: 22px; font-weight: 700; font-style: italic; color: var(--white); line-height: 24px; letter-spacing: 0; }
  .plan--featured .plan-note { left: 43px; top: 48px; color: var(--white); }
  .plan--featured .plan-lead { right: auto; left: 262px; top: 35px; color: var(--ink); }
  .plan--featured .plan-price { right: auto; left: 406px; top: 28px; }
  .plan--featured .plan-unit { left: 481px; top: 35px; color: var(--ink); }
  .plan--featured .buy-btn { left: 593px; top: 23px; }

  /* Feature panel */
  .features { position: absolute; left: 253px; top: 346px; width: 694px; height: 275px; background: var(--panel); border-radius: 0 0 4px 4px; }
  .features-title { position: absolute; left: 38px; top: 30px; font-family: "Lato", sans-serif; font-weight: 700; font-size: 10px; color: var(--ink); }
  .features-rule { position: absolute; left: 19px; top: 51px; width: 656px; height: 1px; background: var(--line); }
  .features-divider { position: absolute; left: 475px; top: 51px; width: 1px; height: 192px; background: var(--line); }
  .feature-list { position: absolute; top: 66px; list-style: none; font-size: 9.3px; color: #5b6270; letter-spacing: .2px; }
  .feature-list li { height: 16.9px; padding-left: 14px; position: relative; }
  .feature-list li::before { content: ""; position: absolute; left: 1px; top: 2px; width: 3px; height: 6px; border-right: 1px solid #9aa1ab; border-bottom: 1px solid #9aa1ab; transform: rotate(40deg); }
  .feature-list li::after { content: ""; position: absolute; left: 5px; top: 2px; width: 3px; height: 6px; border-right: 1px solid #9aa1ab; border-bottom: 1px solid #9aa1ab; transform: rotate(40deg); }
  .feature-list--left { left: 38px; }
  .feature-list--right { left: 256px; }

  .summary { position: absolute; left: 490px; top: 73px; width: 167px; }
  .summary-row { display: flex; justify-content: space-between; align-items: baseline; margin-bottom: 11px; color: var(--ink); }
  .summary-row dt { width: 98px; text-align: right; }
  .summary-row dd { text-align: right; }
  .summary-row.total { font-size: 11px; }
  .summary-row.discount { font-size: 9px; }
  .summary-row.per-video { font-size: 9px; color: var(--royal); }
  .summary-row.grand { font-size: 15px; margin-top: 6px; }
  .summary-row.grand dd { color: var(--price); font-weight: 600; }
  .features .buy-btn { left: 588px; top: 194px; }

  .plan--holiday { top: 627px; }
  .plan--season { top: 702px; }
  .plan--social { top: 777px; }
  .plan--alacarte { top: 196px; }

  /* Footer */
  .site-footer { position: absolute; left: 0; top: 896px; width: 1200px; height: 215px; background: var(--navy); color: var(--white); }
  .footer-brand { position: absolute; left: 253px; top: 54px; }
  .footer-brand .brand-name { font-size: 30px; letter-spacing: 5px; line-height: 30px; color: #dfe6ee; }
  .footer-brand .brand-tag { font-size: 9px; letter-spacing: 1.3px; margin-top: 4px; }
  .footer-slogan { position: absolute; left: 253px; top: 106px; font-family: "Lato", sans-serif; font-weight: 700; font-size: 11.5px; letter-spacing: -.2px; }
  .footer-col { position: absolute; top: 55px; font-family: "Lato", sans-serif; }
  .footer-col h3 { font-size: 11px; font-weight: 400; }
  .footer-col h3::after { content: ""; display: block; width: 16px; height: 1px; background: #5b6577; margin-top: 6px; }
  .quick-links { left: 550px; }
  .quick-links ul { list-style: none; margin-top: 13px; font-size: 9px; }
  .quick-links li { height: 20.7px; }
  .about { left: 728px; width: 220px; }
  .about p { margin-top: 12px; font-size: 10px; line-height: 15.6px; }
  .social { display: flex; gap: 7px; margin-top: 12px; }
  .social span { width: 24px; height: 24px; border-radius: 50%; background: #1e2840; }
</style>
</head>
<body>
  <header class="site-header">
    <div class="brand">
      <div class="brand-name">SURGE</div>
      <div class="brand-tag">MARKETING VIDEOS MADE FOR YOU</div>
    </div>
    <nav class="main-nav">
      <a>Home</a><a>How It Works</a><a>Examples</a><a>FAQ</a><a>Contact Us</a><a class="active">Pricing</a><a>Calendar</a>
    </nav>
    <div class="account"><span class="login">Log In</span><span class="signup">Sign Up</span></div>
  </header>

  <h1 class="page-title">NO HIDDEN CHARGES!</h1>
  <h2 class="page-subtitle">CHOOSE YOUR DEAL!</h2>

  <section class="plan plan--alacarte">
    <div class="plan-tab"><div class="plan-strip"><span class="chevron"></span></div>
      <div class="plan-name">AL A CARTE</div><div class="plan-note">As Needed Basis</div></div>
    <span class="plan-lead">Starts @ From</span>
    <span class="plan-price"><sup>$</sup>37.00</span>
    <span class="plan-unit">Video Format</span>
    <a class="buy-btn">Buy Now!</a>
  </section>

  <section class="plan plan--featured">
    <div class="plan-tab"><div class="plan-strip"><span class="chevron"></span></div>
      <div class="plan-name">Subscription</div><div class="plan-note">New Video Ads Monthly</div></div>
    <span class="plan-lead">Starts @ From</span>
    <span class="plan-price"><sup>$</sup>16.00</span>
    <span class="plan-unit">Video Format</span>
    <a class="buy-btn">Buy Now!</a>
  </section>

  <section class="features">
    <div class="features-title">Included Features</div>
    <div class="features-rule"></div>
    <div class="features-divider"></div>
    <ul class="feature-list feature-list--left">
      <li>Custom Videos</li><li>Price Starts @ $16/Video Format</li><li>24hrs Delivery Speed</li>
      <li>Unlimited Revisions</li><li>Mp4 Full HD 1080p File Formats</li><li>Wide Screen Video Format</li>
      <li>Large Square Video Format</li><li>Vertical Video Format</li><li>Page Cover Video Format</li><li>Holiday Theme Video</li>
    </ul>
    <ul class="feature-list feature-list--right">
      <li>Seasonal Theme Video</li><li>Content Done For You</li><li>Full Branding In Video</li>
      <li>Full Copyright Ownership</li><li>Full Reselling Rights</li><li>Premium Video Clips</li>
      <li>Use My Images</li><li>Use My Video Footage</li><li>Use My Background Music</li><li>Fully Licensed Background Music</li>
    </ul>
    <dl class="summary">
      <div class="summary-row total"><dt>Total:</dt><dd>$99.00</dd></div>
      <div class="summary-row discount"><dt>Discount:</dt><dd>$19.80</dd></div>
      <div class="summary-row per-video"><dt>Price Per Video:</dt><dd>$79.20</dd></div>
      <div class="summary-row grand"><dt>Grand Total:</dt><dd>$79.20</dd></div>
    </dl>
    <a class="buy-btn">Buy Now!</a>
  </section>

  <section class="plan plan--holiday">
    <div class="plan-tab"><div class="plan-strip"><span class="chevron"></span></div>
      <div class="plan-name">HOLIDAY PKG</div><div class="plan-note">17 Holiday Themed Videos</div></div>
    <span class="plan-lead">Only @</span>
    <span class="plan-price"><sup>$</sup>14.00</span>
    <span class="plan-unit">Video Format</span>
    <a class="buy-btn">Buy Now!</a>
  </section>

  <section class="plan plan--season">
    <div class="plan-tab"><div class="plan-strip"><span class="chevron"></span></div>
      <div class="plan-name">SEASON PKG</div><div class="plan-note">4 Seasonal Themed Videos</div></div>
    <span class="plan-lead">Only @</span>
    <span class="plan-price"><sup>$</sup>18.00</span>
    <span class="plan-unit">Video Format</span>
    <a class="buy-btn">Buy Now!</a>
  </section>

  <section class="plan plan--social">
    <div class="plan-tab"><div class="plan-strip"><span class="chevron"></span></div>
      <div class="plan-name">SOCIAL MEDIA</div><div class="plan-note">Daily Videos for your Social Media</div></div>
    <span class="plan-lead">Only @</span>
    <span class="plan-price"><sup>$</sup>10.00</span>
    <span class="plan-unit">Video Format</span>
    <a class="buy-btn">Buy Now!</a>
  </section>

  <footer class="site-footer">
    <div class="footer-brand brand">
      <div class="brand-name">SURGE</div>
      <div class="brand-tag">MARKETING VIDEOS MADE FOR YOU</div>
    </div>
    <div class="footer-slogan">CREATED BY A MARKETER FOR MARKETERS.</div>
    <div class="footer-col quick-links">
      <h3>Quick Links</h3>
      <ul><li>How It Works</li><li>Term Of Service</li><li>Privacy Policy</li><li>Cookies Policy</li></ul>
    </div>
    <div class="footer-col about">
      <h3>About Us</h3>
      <p>With Surge, you simply let us know what you want to promote and we will have your video ad finished as soon as 24 hours!</p>
      <div class="social" aria-label="Social profiles">
        <span></span><span></span><span></span><span></span><span></span>
      </div>
    </div>
  </footer>
</body>
</html>
```